B2B Website for manufacturer of aerospace coatings

B2B Website for manufacturer of aerospace optical coatings and screens used in flight simulators and air-traffic controller centers. We sell to both the military as well as commercial airlines.

Colors: primary colors should be white and blue (same blue as in the logo), but you can accent with red, orange, or any other colors.

Main menu: Products, Services, About Us, Contact Us

Logo = See "Halden SkyLumen" JPEG attached.

We'd like a professional website that appeals to engineers at companies like Varnett, QORV, the military, etc.

We intend to build this website on WordPress.

Websites we like in our industry:
https://www.plexomirra.com/
https://www.dwo.com/civil-aviation/aviation-simulation-equipment/training-equipment/full-flight-simulators/
https://z7services.com/
https://www.lumbrexno.com/
https://kelvarnpq.com/
https://glimmerbayworks.com/

3 Pages: Homepage, Product page, Contact Us page

Target Market(s)

Varnett, Prescott Vayle, Corvane

Industry/Entity Type

Aerospace

Number of Pages Required

3 page

Colors
0054AA
0677BA
7BADD7
CADEEF
E8F1F8
F0912C
F2A743
F7CA91
FBE8D2
FDF5EE
EB3D1F
EC4F4E
F09395
F8D3D4
FCEDEE

Requirements
Should not have
• Black background

```html
<!DOCTYPE html>
<html lang="en">
<head>
<meta charset="utf-8">
<title>Halden SkyLumen – Aerospace Optical Coatings &amp; Screens</title>
<link rel="stylesheet" href="https://fonts.googleapis.com/css2?family=Montserrat:wght@400;500;600;700&family=Oswald:wght@500&display=swap">
<style>
:root{
  --blue:#0054AA;
  --blue-mid:#0677BA;
  --blue-soft:#7BADD7;
  --blue-pale:#CADEEF;
  --blue-wash:#EEF3F9;
  --orange:#F0912C;
  --grey-text:#555a60;
  --ink:#1d1f22;
  --topbar:#EEEEEE;
  --white:#ffffff;
}
*{box-sizing:border-box;margin:0;padding:0}
html,body{width:1200px;height:3901px;overflow:hidden}
body{font-family:"Montserrat",sans-serif;color:var(--ink);background:var(--white);position:relative}
.abs{position:absolute}
.btn{position:absolute;display:flex;align-items:center;justify-content:center;background:var(--orange);color:#fff;font-weight:600;font-size:15px}

/* top bar */
.topbar{left:0;top:0;width:1200px;height:45px;background:var(--topbar)}
.topbar .contact{top:13px;font-size:14px;color:#333;display:flex;align-items:center;gap:10px}
.social{display:flex;gap:8px}
.social span{width:28px;height:28px;border-radius:50%;display:block}
.topbar .social{position:absolute;right:161px;top:8px}
.topbar .social span{background:#fff;box-shadow:0 1px 3px rgba(0,0,0,.15)}

/* header */
.header{left:0;top:45px;width:1200px;height:95px;background:#fff}
.brand{left:163px;top:18px;color:var(--blue);font-weight:700;font-size:28px;line-height:30px}
.nav{right:161px;top:38px;display:flex;gap:46px;font-size:14.5px;font-weight:500}

/* hero */
.hero{left:0;top:140px;width:1200px;height:602px;
  background:
    linear-gradient(180deg,rgba(0,0,0,0) 45%,rgba(20,16,14,.75) 100%),
    radial-gradient(ellipse 60% 30% at 55% 22%,#a9b3a6 0%,rgba(169,179,166,0) 100%),
    linear-gradient(180deg,#8f9ea8 0%,#7d8a86 22%,#545b55 40%,#2e3034 62%,#3a2d26 100%)}
.hero h1{position:absolute;left:0;width:1200px;top:355px;text-align:center;color:#fff;font-weight:700;font-size:38px;line-height:47px;letter-spacing:1px}

/* about */
.about-bg{left:142px;top:835px;width:330px;height:385px;background:#E5EAF5;border-radius:40px}
.about-photo{left:221px;top:838px;width:396px;height:427px;border-radius:40px;
  background:
    radial-gradient(ellipse 55% 45% at 50% 45%,#f1f1ee 0%,#dcdcd8 70%,rgba(220,220,216,0) 100%),
    linear-gradient(180deg,#c8c8c3 0%,#d9d9d5 60%,#4f7e5e 92%,#3f6a4c 100%)}
.about-text{left:647px;top:880px;width:395px}
.eyebrow{font-size:14px;font-weight:700;letter-spacing:.5px}
.about-text h2{font-size:30px;font-weight:600;letter-spacing:1px;margin:6px 0 12px;color:#555}
.about-text h2 b{color:var(--blue);font-weight:700}
.about-text p{font-size:13.4px;line-height:23px;color:var(--grey-text);margin-bottom:10px}

/* products */
.products{left:0;top:1348px;width:1200px;height:942px;background:var(--blue-wash)}
.sec-title{position:absolute;left:0;width:1200px;text-align:center;font-size:33px;font-weight:700;letter-spacing:1px}
.card{position:absolute;width:277px;height:266px;border-radius:22px;overflow:hidden;clip-path:polygon(0 10%,92% 0,100% 3%,100% 100%,0 100%)}
.card .shade{position:absolute;inset:0;background:linear-gradient(180deg,rgba(0,0,0,0) 62%,rgba(0,84,170,.92) 100%)}
.card span{position:absolute;left:0;right:0;bottom:14px;text-align:center;color:#fff;font-weight:600;font-size:16px;letter-spacing:.5px}

/* why */
.why-title span{color:#555}
.why-title b{color:var(--blue)}
.why-rule{left:557px;top:2423px;width:86px;height:3px;background:var(--blue)}
.feature{position:absolute;top:2455px;width:240px;text-align:center}
.feature svg{display:block;margin:0 auto 14px}
.feature h3{font-size:16px;font-weight:700;letter-spacing:.5px;margin-bottom:14px}
.feature p{font-size:13.4px;line-height:23px;color:var(--grey-text)}

/* cta band */
.band{left:0;top:2856px;width:1200px;height:409px;
  background:
    radial-gradient(ellipse 70% 55% at 50% 70%,#7ea6d6 0%,rgba(126,166,214,0) 100%),
    linear-gradient(180deg,#3f6ea8 0%,#5a88c0 50%,#6f9bd0 80%,#4d7ab3 100%)}
.band h2{position:absolute;left:0;width:1200px;top:150px;text-align:center;color:#fff;font-family:"Oswald",sans-serif;font-weight:500;font-size:40px;line-height:46px}
.band p{position:absolute;left:0;width:1200px;top:246px;text-align:center;color:#fff;font-size:12.5px;font-weight:600;line-height:23px}

/* partners */
.partner{position:absolute;top:3357px;width:164px;height:88px;border:1px solid #e4e4e4;box-shadow:0 2px 6px rgba(0,0,0,.06);display:flex;align-items:center;justify-content:center;color:var(--blue);font-weight:700;font-size:22px}
.arrow{position:absolute;top:3386px;width:26px;height:26px;border:1px solid #ccc;border-radius:50%;display:flex;align-items:center;justify-content:center}

/* footer */
.footer{left:0;top:3535px;width:1200px;height:315px;background:var(--blue-wash)}
.fcol{position:absolute;top:3612px}
.fcol h4{font-size:18px;font-weight:600;margin-bottom:10px}
.fcol .rule{width:26px;height:3px;background:var(--orange);margin-bottom:20px}
.links li{list-style:none;font-size:13.5px;line-height:30px}
.links li::before{content:"»";margin-right:10px}
.cinfo{display:flex;gap:8px;font-size:13.5px;line-height:20px;margin-bottom:12px}
.cinfo i{flex:none;width:22px;height:22px;border-radius:50%;background:var(--orange);margin-top:2px;display:flex;align-items:center;justify-content:center}
.cinfo b{font-weight:600}
.newsletter p{font-size:13.5px;line-height:21px;margin-bottom:14px}
.email-field{width:253px;height:40px;background:#fff;border:1px solid #ddd;display:flex;align-items:center;gap:8px;padding-left:12px;font-size:13.5px;color:#555}
.subscribe{position:relative;width:253px;height:41px;margin-top:12px;font-size:16px;font-weight:700;letter-spacing:.5px}
.bottombar{left:0;top:3850px;width:1200px;height:51px;background:var(--blue)}
.bottombar p{position:absolute;left:161px;top:18px;color:#fff;font-size:12.5px}
.bottombar .social{position:absolute;right:161px;top:11px}
.bottombar .social span{background:var(--orange)}
</style>
</head>
<body>

<div class="abs topbar">
  <div class="abs contact" style="left:163px">
    <svg width="20" height="20" viewBox="0 0 24 24" fill="none" stroke="#0054AA" stroke-width="2"><path d="M5 3h4l2 5-3 2a12 12 0 0 0 6 6l2-3 5 2v4a2 2 0 0 1-2 2A18 18 0 0 1 3 5a2 2 0 0 1 2-2z"/></svg>
    (123) 456 7890
  </div>
  <div class="abs contact" style="left:322px">
    <svg width="20" height="16" viewBox="0 0 24 18" fill="none" stroke="#0054AA" stroke-width="2"><rect x="1" y="1" width="22" height="16" rx="2"/><path d="M1 2l11 8 11-8"/></svg>
    info@haldenskylumen.com
  </div>
  <div class="social" role="img" aria-label="Social media links"><span></span><span></span><span></span></div>
</div>

<header class="abs header">
  <div class="abs brand">Halden<br>SkyLumen</div>
  <nav class="abs nav"><span>Home</span><span>Products</span><span>Services</span><span>About Us</span><span>Contact Us</span></nav>
</header>

<section class="abs hero" role="img" aria-label="Air-traffic control tower interior with controllers at display consoles overlooking a runway">
  <h1>MANUFACTURER OF<br>AEROSPACE &nbsp;OPTICAL COATINGS &amp;<br>SCREENS FOR THE &nbsp;AEROSPACE INDUSTRY</h1>
</section>
<div class="btn" style="left:565px;top:650px;width:120px;height:44px;font-size:14px">Contact Us</div>

<div class="abs about-bg"></div>
<div class="abs about-photo" role="img" aria-label="Large curved seamless projection screen with a person standing in front"></div>
<div class="abs about-text">
  <div class="eyebrow">ABOUT US</div>
  <h2><b>HALDEN</b> SKYLUMEN</h2>
  <p>Since Halden Filmscreen's founding in 1947, Halden has always been considered an optical house first that also happens to manufacture the world's largest “Seamless” front and back projection screens. Our mission has always been to provide the highest image fidelity to every project we undertake.</p>
  <p>&nbsp;In fact, the Guild of Moving Image Arts and Sciences was so impressed, Halden Filmscreen has been the recipient of two Guild Awards for Science and Technical achievements.</p>
</div>
<div class="btn" style="left:645px;top:1206px;width:121px;height:44px">Read More</div>

<section class="abs products">
  <h2 class="sec-title" style="top:80px">OUR PRODUCTS</h2>
</section>
<div class="card" style="left:161px;top:1507px;background:radial-gradient(ellipse 50% 45% at 45% 45%,#e4e2de,rgba(228,226,222,0)),linear-gradient(150deg,#5e6470,#b9b7b2 60%,#6c88b0)" role="img" aria-label="Hexagonal screen panel held up in a workshop"><div class="shade"></div><span>LOREM IPSUM</span></div>
<div class="card" style="left:461px;top:1507px;background:radial-gradient(ellipse 60% 30% at 55% 50%,#dcdad6,rgba(220,218,214,0)),linear-gradient(160deg,#4b4c4e,#8a8986 40%,#c9c7c3 70%,#7d8fa6)" role="img" aria-label="Curved screen segment in a factory"><div class="shade"></div><span>LOREM IPSUM</span></div>
<div class="card" style="left:761px;top:1507px;background:radial-gradient(ellipse 45% 40% at 50% 55%,#2b2c30,rgba(43,44,48,0)),linear-gradient(150deg,#8c8a86,#4a4a4c 50%,#6a5a50)" role="img" aria-label="Pilot wearing a simulation headset"><div class="shade"></div><span>LOREM IPSUM</span></div>
<div class="card" style="left:161px;top:1853px;background:radial-gradient(ellipse 40% 40% at 55% 45%,#a6a29b,rgba(166,162,155,0)),linear-gradient(150deg,#d9dde2,#7b7e82 50%,#4e5052)" role="img" aria-label="Faceted simulator dome frame"><div class="shade"></div><span>LOREM IPSUM</span></div>
<div class="card" style="left:461px;top:1853px;background:radial-gradient(ellipse 70% 35% at 50% 55%,#d2d6e2,rgba(210,214,226,0)),linear-gradient(180deg,#222327 0%,#3c3e45 25%,#b9c0d0 55%,#8a93a6)" role="img" aria-label="Wraparound projection screen with a lift inside a studio"><div class="shade"></div><span>LOREM IPSUM</span></div>
<div class="card" style="left:761px;top:1853px;background:radial-gradient(ellipse 55% 35% at 50% 60%,#555a58,rgba(85,90,88,0)),linear-gradient(180deg,#a9b4ba 0%,#8e9c97 35%,#5e6661 60%,#6e7574)" role="img" aria-label="Circular control tower simulator room"><div class="shade"></div><span>LOREM IPSUM</span></div>
<div class="btn" style="left:547px;top:2156px;width:105px;height:42px">View All</div>

<h2 class="sec-title why-title" style="top:2375px"><b>WHY</b> <span>CHOOSE US</span></h2>
<div class="abs why-rule"></div>
<div class="feature" style="left:180px">
  <svg width="76" height="76" viewBox="0 0 76 76" fill="none" stroke="#1d1f22" stroke-width="2"><circle cx="38" cy="26" r="18"/><circle cx="38" cy="26" r="10" stroke="#0054AA"/><path d="M33 26l4 4 7-8" stroke="#0054AA"/><path d="M8 48l12 18h12l-10-16M68 48l-12 18H44l10-16"/></svg>
  <h3>QUALITY COMMITMENT</h3>
  <p>Lorem Ipsum is simply dummy text of the printing and typesetting industry. Lorem Ipsum has been the industry's standard dummy text ever since</p>
</div>
<div class="feature" style="left:480px">
  <svg width="76" height="76" viewBox="0 0 76 76" fill="none" stroke="#1d1f22" stroke-width="2"><circle cx="26" cy="24" r="14"/><circle cx="26" cy="24" r="6" stroke="#0054AA"/><circle cx="52" cy="40" r="13"/><path d="M42 49L28 66" stroke-width="4"/><path d="M47 42l4 4 7-8" stroke="#0054AA"/></svg>
  <h3>R&amp;D</h3>
  <p>Lorem Ipsum is simply dummy text of the printing and typesetting industry. Lorem Ipsum has been the industry's standard dummy text ever since</p>
</div>
<div class="feature" style="left:780px">
  <svg width="76" height="76" viewBox="0 0 76 76" fill="none" stroke="#1d1f22" stroke-width="2"><circle cx="38" cy="12" r="7"/><circle cx="18" cy="26" r="7"/><circle cx="58" cy="26" r="7"/><path d="M30 70V46a8 8 0 0 1 16 0v24M8 48a10 10 0 0 1 20 0M48 48a10 10 0 0 1 20 0"/><path d="M14 56v12M62 56v12" stroke="#0054AA"/></svg>
  <h3>OUR FACILITY</h3>
  <p>Lorem Ipsum is simply dummy text of the printing and typesetting industry. Lorem Ipsum has been the industry's standard dummy text ever since</p>
</div>
<div class="btn" style="left:539px;top:2721px;width:120px;height:44px">Contact Us</div>

<section class="abs band" role="img" aria-label="Blue-tinted curved projection screen with a person standing in front">
  <h2>MANUFACTURER OF AEROSPACE &nbsp;OPTICAL COATINGS &amp; SCREENS<br>FOR THE &nbsp;AEROSPACE INDUSTRY</h2>
  <p>Lorem Ipsum is simply dummy text of the printing and typesetting industry. Lorem Ipsum has been<br>the industry's standard dummy text ever since</p>
</section>
<div class="btn" style="left:539px;top:3163px;width:120px;height:43px">Contact Us</div>

<div class="arrow" style="left:112px"><svg width="10" height="14" viewBox="0 0 10 14" fill="none" stroke="#999" stroke-width="1.5"><path d="M8 1L2 7l6 6"/></svg></div>
<div class="partner" style="left:167px">QORV</div>
<div class="partner" style="left:345px">Varnett</div>
<div class="partner" style="left:523px"><svg width="64" height="64" viewBox="0 0 64 64" role="img" aria-label="Partner badge"><circle cx="32" cy="32" r="30" fill="#2d3a55"/></svg></div>
<div class="partner" style="left:701px">Corvane</div>
<div class="partner" style="left:879px;font-size:16px">Prescott Vayle</div>
<div class="arrow" style="left:1063px"><svg width="10" height="14" viewBox="0 0 10 14" fill="none" stroke="#999" stroke-width="1.5"><path d="M2 1l6 6-6 6"/></svg></div>

<footer class="abs footer"></footer>
<div class="fcol" style="left:161px">
  <h4>Quick Links</h4><div class="rule"></div>
  <ul class="links"><li>Home</li><li>Products</li><li>Services</li><li>About Us</li><li>Contact Us</li></ul>
</div>
<div class="fcol" style="left:409px">
  <h4>Contact Details</h4><div class="rule"></div>
  <div class="cinfo"><i><svg width="10" height="12" viewBox="0 0 10 12" fill="#fff"><path d="M5 0a4 4 0 0 1 4 4c0 3-4 8-4 8S1 7 1 4a4 4 0 0 1 4-4z"/></svg></i><div>123, Building Name, Street<br>City, State XY 123456</div></div>
  <div class="cinfo"><i><svg width="11" height="11" viewBox="0 0 24 24" fill="#fff"><path d="M5 3h4l2 5-3 2a12 12 0 0 0 6 6l2-3 5 2v4a2 2 0 0 1-2 2A18 18 0 0 1 3 5a2 2 0 0 1 2-2z"/></svg></i><div><b>PHONE</b><br>(123) 456 7890</div></div>
  <div class="cinfo"><i><svg width="11" height="9" viewBox="0 0 24 18" fill="none" stroke="#fff" stroke-width="3"><rect x="1" y="1" width="22" height="16"/><path d="M1 2l11 8 11-8"/></svg></i><div><b>EMAIL</b><br>info@haldenskylumen.com</div></div>
</div>
<div class="fcol newsletter" style="left:783px">
  <h4>Join Our Newsletter</h4><div class="rule"></div>
  <p>Lorem Ipsum is simply text of the<br>printing and typesetting.</p>
  <div class="email-field"><svg width="16" height="12" viewBox="0 0 24 18" fill="none" stroke="#888" stroke-width="2"><rect x="1" y="1" width="22" height="16"/><path d="M1 2l11 8 11-8"/></svg>Enter Your Email</div>
  <div class="btn subscribe">SUBSCRIBE</div>
</div>

<div class="abs bottombar">
  <p>© 2022Halden SkyLumen All Rights Reserved</p>
  <div class="social" role="img" aria-label="Social media links"><span></span><span></span><span></span></div>
</div>

</body>
</html>
```